Social Media Graphics - ALL TEXT RV

We are looking for a series of social media graphics for Pixaloom (standard size 1:1 (1080x1080px) that are ALL TEXT. We want the following quotes below on each graphic; one quote per graphic. AND, In very small letters at the bottom of each graphic, add @RVCarltonLive

The look and feel of these graphics should be complimentary to the color palette attached below; but keep them simple. But the design is up to you; at the end of this document, I provided various samples of all text graphics that I like as examples.

Target Market(s)

women looking to lose weight

Industry/Entity Type

health and wellness

Colors
E54698
E96AAD
F1A4CE
F9D9EA
FCEFF6

Requirements
Must have
• the quotes in the document
Should not have
• no stock photography

```html
<!DOCTYPE html>
<html lang="en">
<head>
<meta charset="utf-8">
<title>RV — All Text Social Graphics</title>
<link href="https://fonts.googleapis.com/css2?family=Montserrat:wght@700;800&display=swap" rel="stylesheet">
<style>
  :root {
    --plum: #6a0a5e;
    --magenta: #b00a7c;
    --hot-pink: #ee0c80;
    --blush: #f7b8db;
    --white: #ffffff;
    --page: #ffffff;
  }
  * { box-sizing: border-box; margin: 0; padding: 0; }
  html, body {
    width: 1194px; height: 1200px; overflow: hidden;
    background: var(--page);
  }
  .board { position: relative; width: 1194px; height: 1200px; }

  .post {
    position: absolute;
    overflow: hidden;
    background: linear-gradient(135deg, var(--plum) 0%, var(--magenta) 40%, var(--hot-pink) 80%, var(--hot-pink) 100%);
    font-family: "Montserrat", "Helvetica Neue", Arial, sans-serif;
    font-weight: 700;
    text-transform: uppercase;
    color: var(--white);
  }
  .post--small { width: 288px; height: 288px; }
  .post--large { width: 560px; height: 560px; }

  .post__frame {
    position: absolute;
    top: 9.6%; left: 10.8%; right: 9.6%; bottom: 12.7%;
    border: 1px solid rgba(255,255,255,0.9);
  }
  .post--large .post__frame { border-width: 2px; }

  .quote {
    position: absolute;
    top: 48.5%;
    left: var(--inset);
    transform: translateY(-50%);
    white-space: nowrap;
    letter-spacing: 0.01em;
  }
  .post--small .quote { font-size: 14.5px; line-height: 18.8px; }
  .post--large .quote { font-size: 29px; line-height: 36.5px; }

  .quote__lead { color: var(--blush); }
  .quote__rest { color: var(--white); }

  .post__handle {
    position: absolute; left: 0; right: 0;
    text-align: center;
    text-transform: none;
    font-weight: 700;
    color: var(--white);
  }
  .post--small .post__handle { bottom: 10px; font-size: 8px; }
  .post--large .post__handle { bottom: 30px; font-size: 15.5px; letter-spacing: 0.02em; }
</style>
</head>
<body>
<main class="board">

  <!-- top row -->
  <article class="post post--small" style="left:0;top:6px">
    <div class="post__frame"></div>
    <p class="quote" style="--inset:72px">
      <span class="quote__lead">Wake up<br>tomorrow<br>with a flatter<br>belly- </span><span class="quote__rest">yes,<br>this overnight<br>remedy works<br>like magic!</span>
    </p>
    <p class="post__handle">@RVCarltonLive</p>
  </article>

  <article class="post post--small" style="left:302px;top:6px">
    <div class="post__frame"></div>
    <p class="quote" style="--inset:55px">
      <span class="quote__lead">Struggling<br>with bloating<br>and belly fat?</span><br><span class="quote__rest">Try this<br>natural solution<br>tonight, and<br>wake up feeling<br>lighter!</span>
    </p>
    <p class="post__handle">@RVCarltonLive</p>
  </article>

  <article class="post post--small" style="left:603px;top:6px">
    <div class="post__frame"></div>
    <p class="quote" style="--inset:59px">
      <span class="quote__lead">One supplement,<br>one night;<br>your belly bloat<br>could be gone<br>by morning.</span><br><span class="quote__rest">Here's how<br>it works!</span>
    </p>
    <p class="post__handle">@RVCarltonLive</p>
  </article>

  <article class="post post--small" style="left:905px;top:6px">
    <div class="post__frame"></div>
    <p class="quote" style="--inset:66px">
      <span class="quote__lead">Finally-</span><br><span class="quote__rest">a natural<br>solution that<br>flattens your<br>belly and eases<br>stomach bloat</span>
    </p>
    <p class="post__handle">@RVCarltonLive</p>
  </article>

  <!-- feature row -->
  <article class="post post--large" style="left:22px;top:321px">
    <div class="post__frame"></div>
    <p class="quote" style="--inset:122px">
      <span class="quote__lead">Sis, your<br>hormones are<br>out of whack -</span><br><span class="quote__rest">that's why<br>the weight won't<br>budge!</span>
    </p>
    <p class="post__handle">@RVCarltonLive</p>
  </article>

  <article class="post post--large" style="left:612px;top:321px">
    <div class="post__frame"></div>
    <p class="quote" style="--inset:106px">
      <span class="quote__lead">Frustrated<br>with belly fat<br>that won't budge?</span><br><span class="quote__rest">I've got the<br>solution that<br>finally worked<br>for me-<br>no crazy<br>diets required.</span>
    </p>
    <p class="post__handle">@RVCarltonLive</p>
  </article>

  <!-- bottom row -->
  <article class="post post--small" style="left:0;top:911px">
    <div class="post__frame"></div>
    <p class="quote" style="--inset:66px">
      <span class="quote__lead">That stubborn<br>belly fat isn't<br>your fault -</span><br><span class="quote__rest">here's what no<br>one tells you.</span>
    </p>
    <p class="post__handle">@RVCarltonLive</p>
  </article>

  <article class="post post--small" style="left:302px;top:911px">
    <div class="post__frame"></div>
    <p class="quote" style="--inset:66px">
      <span class="quote__lead">You've been<br>lied to - 'just<br>eat less and<br>exercise more'</span><br><span class="quote__rest">doesn't work in<br>menopause</span>
    </p>
    <p class="post__handle">@RVCarltonLive</p>
  </article>

  <article class="post post--small" style="left:603px;top:911px">
    <div class="post__frame"></div>
    <p class="quote" style="--inset:57px">
      <span class="quote__lead">A natural way<br>to boost GLP-1 -<br>no injections,<br>no side effects,<br>just real results.</span><br><span class="quote__rest">Here's how<br>it works.</span>
    </p>
    <p class="post__handle">@RVCarltonLive</p>
  </article>

  <article class="post post--small" style="left:905px;top:911px">
    <div class="post__frame"></div>
    <p class="quote" style="--inset:55px">
      <span class="quote__lead">GLP-1 : the magic<br>behind the weight<br>loss drugs. But<br>here's the secret -</span><br><span class="quote__rest">you can boost<br>it naturally<br>without a<br>prescription!</span>
    </p>
    <p class="post__handle">@RVCarltonLive</p>
  </article>

</main>
</body>
</html>
```